Spices producer needs product label design.

I need a two label design of 90mm(H) x 60mm(H) for multiple line of spices and other product. First label for the front should have the logo, and second label should be the same as the first but without the logo. I would like the same dark reddish colour on my logo for the design if possible or similar. This label will be use for multiple products, so a clear in-between space is important to add information and change product name for printing . I would prefer a mixture of traditional and rustic style.
I have attached my logos and sample on how I would like the look.

Target Market(s)

25-60 women and men.

Industry/Entity Type

Retail

Requirements
Must have
• As stated above.
Nice to have
• Please see attached sample .
Should not have
• Multiple colours, animation design.

```html
<!DOCTYPE html>
<html lang="en">
<head>
<meta charset="utf-8">
<title>KORVA Natural Spices Label</title>
<link rel="stylesheet" href="https://fonts.googleapis.com/css2?family=Bebas+Neue&display=swap">
<style>
  :root {
    --page: #ffffff;
    --label-red-deep: #a8181f;
    --label-red: #c11f27;
    --label-red-light: #cf2630;
    --band-red: #7a1014;
    --gold-dark: #b8862e;
    --gold-light: #f3d58a;
    --ink-light: #ffffff;
  }
  * { margin: 0; padding: 0; box-sizing: border-box; }
  html, body {
    width: 1200px;
    height: 800px;
    overflow: hidden;
    background: var(--page);
  }
  .label {
    position: absolute;
    left: 40px;
    top: 26px;
    width: 1118px;
    height: 746px;
    overflow: hidden;
  }
  .label__texture {
    position: absolute;
    inset: 0;
    background:
      radial-gradient(ellipse at 75% 45%, var(--label-red-light) 0%, transparent 60%),
      linear-gradient(90deg, var(--label-red-deep) 0%, var(--label-red) 55%, var(--label-red-light) 100%);
  }
  .label__brand {
    position: absolute;
    left: 0;
    right: 0;
    top: 200px;
    text-align: center;
    font-family: "Bebas Neue", sans-serif;
    font-size: 150px;
    line-height: 1;
    letter-spacing: 6px;
    color: var(--ink-light);
  }
  .label__band {
    position: absolute;
    left: 0;
    right: 0;
    top: 432px;
    height: 121px;
    background: var(--band-red);
    display: flex;
    align-items: center;
    justify-content: center;
  }
  .label__rule {
    position: absolute;
    left: 0;
    right: 0;
    height: 4px;
    background: linear-gradient(90deg, var(--gold-dark), var(--gold-light) 30%, var(--gold-dark) 60%, var(--gold-light) 85%, var(--gold-dark));
  }
  .label__rule--top { top: 5px; }
  .label__rule--bottom { bottom: 5px; }
  .label__product {
    font-family: "Bebas Neue", sans-serif;
    font-size: 92px;
    line-height: 1;
    letter-spacing: 1px;
    color: var(--ink-light);
    padding-top: 6px;
  }
</style>
</head>
<body>
  <main class="label">
    <div class="label__texture" role="img" aria-label="Red background with a traditional overlapping wave-scale pattern"></div>
    <div class="label__brand">KORVA</div>
    <section class="label__band">
      <span class="label__rule label__rule--top"></span>
      <h1 class="label__product">NATURAL SPICES</h1>
      <span class="label__rule label__rule--bottom"></span>
    </section>
  </main>
</body>
</html>
```